◆遺体の目的/概要
電子書籍(novrel)の表紙のデザインをお願いします。

◆画像のサイズ
表紙ファイルの理想的な寸法は2,560✕1,600ピクセルです。
注:画像の寸法は1,000✕625ピクセル以上であることが必要です。
画像の最大の寸法は10,000✕10,000ピクセルです。

◆タイトル
外国人と一緒に働くすべての人へ
「ソラーレ・ポルト・メトリクス」
Solare Porto Metrics
少子高齢化の社会を生き残る強い会社を作る方法

◆著者
外国人ブリッジコーディネーター
橋本 健吾

◆本の内容
少子高齢化が進む社会にあって、
外国人労働者の必要性や、彼らが働きやす職場環境作りの必要性
どんなコミュニケーションが必要かという事を解説した本です。
※本文を参考資料として添付します。

◆デザイン要望
会社や企業向けなので、プロフェッショナルなイメージ
グローバルなイメージ(目を引く外国人の写真など)
でよろしくお願い致します。

※次点、次々点の方への参加報酬も設定いたします。

※その他、必要な情報がありましたらお問い合せください。

本文の内容に該当する登場人物のイメージを用いている点や
「強い会社を作る」という主なテーマが強調されていいる点など、
ぱっと見て分かりやすいものを選ばせていただきました。

ほんとにどれもセンスを感じられるものだったので、
選定するのに、とても時間がかかりました。
同じテーマで、こんなにも色々なアイデアがあること
その多様性に感動しました。
皆さんが時間をかけて、考えてくださったことに感謝致します。
今後も出版を考えていますので、また依頼の際は多くの方の提案をよろしくお願い致します!

```html
<!DOCTYPE html>
<html lang="ja">
<head>
<meta charset="utf-8">
<title>ソラーレ・ポルト・メトリクス 表紙</title>
<link rel="stylesheet" href="https://fonts.googleapis.com/css2?family=Oswald:wght@600;700&family=Noto+Sans+JP:wght@500;700;900&family=Noto+Serif+JP:wght@700;900&family=Great+Vibes&display=swap">
<style>
  :root {
    --ink: #1a1a1a;
    --gold: #c7a06a;
    --accent: #e39a2a;
    --corner: #f3d37c;
    --paper: #ffffff;
    --map-a: #f6c9d4;
    --map-b: #bfe3f0;
    --map-c: #f7e9a8;
    --people-a: #d8d3cf;
    --people-b: #6b6f78;
  }
  * { margin: 0; padding: 0; box-sizing: border-box; }
  html, body { width: 750px; height: 1200px; overflow: hidden; background: var(--paper); }
  .cover { position: relative; width: 750px; height: 1200px; background: var(--paper); overflow: hidden; color: var(--ink); font-family: "Noto Sans JP", sans-serif; }
  .corner { position: absolute; left: 0; top: 0; z-index: 2; }
  .text { position: absolute; z-index: 3; }
  .audience { top: 26px; left: 0; width: 100%; text-align: center; font-weight: 700; font-size: 34px; letter-spacing: 2px; }
  .audience em { font-style: normal; color: var(--accent); font-size: 38px; }
  .en-title { left: 0; width: 100%; text-align: center; font-family: "Oswald", sans-serif; font-weight: 700; line-height: 1; }
  .en-title.line1 { top: 118px; font-size: 150px; letter-spacing: 4px; color: var(--ink); }
  .en-title.line2 { top: 248px; font-size: 138px; letter-spacing: 4px; color: var(--gold); }
  .en-script { top: 272px; left: 330px; font-family: "Great Vibes", cursive; font-size: 84px; color: var(--ink); transform: rotate(-6deg); }
  .jp-title { top: 400px; left: 0; width: 100%; text-align: center; font-weight: 900; font-size: 50px; line-height: 1.22; letter-spacing: 2px; }
  .subtitle-pill { top: 530px; left: 50%; transform: translateX(-50%); border: 2px solid var(--ink); border-radius: 30px; padding: 6px 36px; font-weight: 700; font-size: 28px; white-space: nowrap; background: var(--paper); }
  .main-theme { top: 585px; left: 0; width: 100%; text-align: center; font-family: "Noto Serif JP", serif; font-weight: 900; font-size: 76px; letter-spacing: 2px; }
  .main-theme .small { font-size: 58px; }
  .world-map { position: absolute; z-index: 1; top: 700px; left: 250px; width: 480px; height: 210px; border-radius: 40% 50% 30% 40%; background: radial-gradient(circle at 30% 40%, var(--map-a), transparent 60%), radial-gradient(circle at 70% 50%, var(--map-b), transparent 60%), radial-gradient(circle at 50% 70%, var(--map-c), transparent 60%); opacity: .75; }
  .team-photo { position: absolute; z-index: 1; top: 880px; left: 20px; width: 710px; height: 320px; background: linear-gradient(180deg, var(--people-a) 0%, var(--people-b) 100%); border-radius: 110px 110px 0 0; }
  .author { top: 790px; left: 52px; font-family: "Noto Serif JP", serif; font-weight: 700; }
  .author .label { font-size: 22px; letter-spacing: 6px; }
  .author .role { font-family: "Noto Sans JP", sans-serif; font-size: 16px; margin-top: 2px; }
  .author .name { font-size: 34px; font-weight: 900; letter-spacing: 4px; margin-top: 0; }
</style>
</head>
<body>
<main class="cover">
  <svg class="corner" width="110" height="110" viewBox="0 0 110 110" aria-hidden="true"><polygon points="0,0 110,0 0,110" fill="var(--corner)"/></svg>
  <div class="world-map" role="img" aria-label="パステルカラーの世界地図"></div>
  <div class="team-photo" role="img" aria-label="並んで立つ多国籍のビジネスパーソンたちの写真"></div>
  <p class="text audience">外国人と<em>一緒</em>に<em>働く</em>すべての人へ</p>
  <div class="text en-title line1">SOLARE</div>
  <div class="text en-title line2">PORTO</div>
  <div class="text en-script">Metrics</div>
  <h1 class="text jp-title">ソラーレ・ポルト<br>メトリクス</h1>
  <p class="text subtitle-pill">少子高齢化の社会を生き残る</p>
  <p class="text main-theme">強<span class="small">い</span>会社を作る方法</p>
  <div class="text author">
    <p class="label">著者</p>
    <p class="role">外国人ブリッジコーディネーター</p>
    <p class="name">橋本 健吾</p>
  </div>
</main>
</body>
</html>
```